Granite Tile Retail Website

We need wireframe PSD for a website selling granite tile. There are 4 custom pages, shopping cart page, and checkout page. I have a logo designed but the color scheme is up to you.
Please look at design-explanation.docx as I got through each page with more detail.
Home - I mocked up the home page so you know the layout (lg-home.jpg). This is where I need you to spend the most time to make a very appealing design.
Color Gallery - We have approximately 20 different stone colors. Each color will have a little gallery of its own pictures. On this page the customer can also add a sample piece of the color they are viewing to their shopping cart.
Questions Page - This page has 3 elements
1. Upload or fax diagram of kitchen for quotation
2. Installation video
3. Installation FAQ (text)
Order Page - This page has 3 steps for the customer
1. Customer chooses his color.
2. For each color we have numerous different products. He inputs the quantity of each product.
3. Customer is given total price and shipping quote. If order over $500 it says "This order qualifies for free shipping". Customer can click on button to "Order Now"
Shopping Cart - Very standard, just like I have attached here. Just modify for your colors / font.
Checkout - Just like in the attached. See design-explanation.docx for minor adjustments.
I have vector file for logo.
Updates
Please try to post your designs by tonightÂ
Target Market(s)
Home owners 40-60 years old
Industry/Entity Type
Shopping
Look and feel

```html
<!DOCTYPE html>
<html lang="en">
<head>
<meta charset="utf-8">
<title>Stonecrest Granite – Home</title>
<link href="https://fonts.googleapis.com/css2?family=Arimo:wght@400;700&family=Varela+Round&family=Cabin:wght@700&display=swap" rel="stylesheet">
<style>
:root{
  --crimson:#a3002a;
  --crimson-dark:#6e0a22;
  --maroon:#6d0d2b;
  --sky:#1aa3d9;
  --blue-btn:#3c97de;
  --slate:#474d55;
  --panel:#f4f4f4;
  --text:#111;
  --muted:#8a8a8a;
  --body:#3a3a3a;
  --link:#1c9bd5;
}
*{margin:0;padding:0;box-sizing:border-box}
html,body{width:1200px;height:1176px;overflow:hidden}
body{position:relative;font-family:"Arimo",Arial,sans-serif;color:var(--text);
  background:linear-gradient(180deg,#e7e1d8 0,#ddd2c0 12%,#c9b79a 40%,#b89a70 70%,#cbbb9c 100%)}
.abs{position:absolute}
.stone-bg{left:0;top:0;width:1200px;height:1176px}

.logo{left:153px;top:32px;font-family:"Arimo",sans-serif;font-weight:700;font-size:32px;color:var(--crimson);letter-spacing:-0.5px}
.utility{right:353px;top:36px;text-align:right;font-size:11px;color:#666;line-height:14px;letter-spacing:.2px}
.utility .hl{color:var(--link)}
.search{left:862px;top:35px;width:217px;height:24px;border:1px solid #d9d9d9;background:#fff}
.search .go{position:absolute;right:-1px;top:-1px;width:25px;height:24px;background:var(--crimson);display:flex;align-items:center;justify-content:center}

.nav{left:122px;top:97px;width:957px;height:42px;background:var(--crimson);border-bottom:3px solid var(--crimson-dark);display:flex;align-items:center;font-family:"Varela Round",sans-serif;font-size:17px;color:#fff}
.nav .item{padding:0 16px;line-height:42px}
.nav .item.active{background:var(--sky);margin-left:16px;padding:0 16px}
.nav .cart{position:absolute;right:0;top:0;height:42px;width:166px;background:var(--crimson-dark);clip-path:polygon(12px 0,100% 0,100% 100%,12px 100%,0 0);display:flex;align-items:center;padding-left:38px;font-family:"Arimo",sans-serif;font-size:12px;color:#d42b4f;gap:6px}

.hero{left:122px;top:142px;width:957px;height:470px;background:var(--panel)}
.feature-frame{left:140px;top:158px;width:485px;height:304px;background:#fff;box-shadow:0 1px 3px rgba(0,0,0,.25)}
.feature-photo{left:149px;top:167px;width:467px;height:286px;background:linear-gradient(160deg,#7c4a2c 0,#9a6a45 30%,#a89277 55%,#6d4c36 80%,#4a2a1a 100%)}
.ribbon{left:143px;top:152px;width:135px;height:132px;overflow:hidden}
.ribbon .band{position:absolute;left:-40px;top:44px;width:210px;height:30px;background:var(--crimson);transform:rotate(-45deg);color:#fff;font-size:10px;text-align:center;line-height:30px;letter-spacing:.4px}
.hero-title{left:653px;top:202px;width:410px;font-size:28px;font-weight:700;line-height:32px;letter-spacing:-0.6px}
.hero-text{left:653px;top:278px;width:400px;font-size:15px;line-height:22.5px;color:var(--muted)}
.btn{display:flex;align-items:center;justify-content:center;color:#fff;font-size:15px;border-radius:2px}
.btn-sample{left:653px;top:368px;width:157px;height:33px;background:linear-gradient(#c2002f,#99001f)}
.btn-all{left:825px;top:366px;width:166px;height:33px;background:linear-gradient(#5a6068,#3b4047)}

.thumbs{left:140px;top:481px;width:920px;height:83px;display:flex;gap:3px}
.thumb{flex:1;background:#fff;padding:8px}
.thumb.active{background:var(--link);padding:6px 8px}
.thumb .img{width:100%;height:100%}
.thumb-caption{top:577px;width:230px;text-align:center;font-size:13px;color:#333}
.thumb-caption.active{color:var(--link)}
.pointer{left:250px;top:474px;width:0;height:0;border:7px solid transparent;border-bottom-color:var(--link);border-top:0}

.content{left:122px;top:624px;width:957px;height:419px;background:var(--panel)}
.intro-title{left:158px;top:675px;width:600px;font-size:19px;line-height:24px;letter-spacing:-0.3px}
.intro-text{left:158px;top:729px;width:580px;font-size:13px;line-height:19px;color:var(--body)}
.showcase-title{left:158px;top:831px;font-size:19px;letter-spacing:-0.3px}
.tile{top:869px;width:129px;height:128px}
.tile .arrow{position:absolute;right:0;top:44px;width:26px;height:28px;background:#fff;display:flex;align-items:center;justify-content:center}
.sale{left:777px;top:679px;width:283px;height:122px;background:linear-gradient(180deg,#5b4636 0,#7a6350 45%,#5d5f68 70%,#4e5058 100%)}
.sale .l1{position:absolute;left:0;right:0;top:70px;text-align:center;color:#d7213f;font-size:18px;letter-spacing:.5px}
.sale .l2{position:absolute;left:0;right:0;top:92px;text-align:center;color:#fff;font-size:19px;letter-spacing:.5px}
.cta{height:35px;display:flex;align-items:center;padding-left:32px;gap:16px;font-family:"Cabin",sans-serif;font-weight:700;font-size:18px;color:#fff;text-shadow:0 1px 1px rgba(0,0,0,.35);box-shadow:1px 2px 3px rgba(0,0,0,.3)}
.cta-blue{left:778px;top:817px;width:247px;background:linear-gradient(#58acea,#2f86d2)}
.cta-grey1{left:778px;top:861px;width:228px;background:linear-gradient(#a9a9a9,#8a8a8a)}
.cta-grey2{left:776px;top:907px;width:181px;background:linear-gradient(#a9a9a9,#8a8a8a)}
.side-tab{left:1139px;top:836px;font-size:11px;color:#222;white-space:nowrap}

.footer{left:122px;top:1043px;width:957px;height:133px;background:linear-gradient(#e2e2e2,#f2f2f2)}
.foot-bar{background:var(--maroon);color:#e8dfe2;font-size:11.5px;display:flex;align-items:center;gap:11px;letter-spacing:.2px}
.foot-bar-1{left:141px;top:1061px;width:437px;height:28px;padding-left:25px;border-left:10px solid #5a0a23}
.foot-bar-2{left:141px;top:1092px;width:471px;height:28px;padding-left:17px}
.copyright{left:154px;top:1135px;font-size:10px;color:#111;word-spacing:1px}
.copyright span{margin-left:18px}
.social{right:135px;font-size:11.5px;color:#222;display:flex;align-items:center;gap:9px;letter-spacing:.2px}
.social .dot{width:21px;height:21px;border-radius:50%;background:#c4c4c4}
</style>
</head>
<body>
<div class="abs stone-bg" role="img" aria-label="Background texture of large tan and grey flagstone rock"></div>

<div class="abs logo">Stonecrest Granite</div>
<div class="abs utility">
  <span class="hl">View all items Checkout</span> &nbsp;|&nbsp; Wishlist &nbsp;|&nbsp; Customer Service &nbsp;1-800-555-0142<br>Register or Login
</div>
<div class="abs search">
  <div class="go"><svg width="13" height="13" viewBox="0 0 13 13"><circle cx="5.5" cy="5.5" r="4" fill="none" stroke="#fff" stroke-width="1.8"/><line x1="8.5" y1="8.5" x2="12" y2="12" stroke="#fff" stroke-width="2"/></svg></div>
</div>

<nav class="abs nav">
  <span class="item active">Home</span>
  <span class="item">Gallery</span>
  <span class="item">Questions</span>
  <span class="item">Order</span>
  <span class="item">My Account</span>
  <span class="item">Shopping Cart</span>
  <span class="item">Sign In</span>
  <div class="cart">
    <svg width="14" height="12" viewBox="0 0 14 12"><path d="M0 1h3l2 7h7l2-5H4" fill="none" stroke="#d42b4f" stroke-width="1.5"/><circle cx="6" cy="10.5" r="1.2" fill="#d42b4f"/><circle cx="11" cy="10.5" r="1.2" fill="#d42b4f"/></svg>
    MY CART &nbsp; 03
  </div>
</nav>

<section class="abs hero"></section>
<div class="abs feature-frame"></div>
<div class="abs feature-photo" role="img" aria-label="Kitchen with a large polished brown granite island and wooden cabinets"></div>
<div class="abs ribbon"><div class="band">FEATURED PRODUCTS</div></div>
<h1 class="abs hero-title">Welcome to Stonecrest Granite Ipsum Dolor is Sit Amet Beauty</h1>
<p class="abs hero-text">Bring the cosmos in your home, Order your FREE sample today to in-vision your home cladded with this beauty Bring the cosmos in your home.</p>
<div class="abs btn btn-sample">Order A Sample</div>
<div class="abs btn btn-all">View All Products</div>

<div class="abs pointer"></div>
<div class="abs thumbs">
  <div class="thumb active"><div class="img" role="img" aria-label="Kitchen granite countertop" style="background:linear-gradient(135deg,#5a3a28,#8f7a62,#4a3326)"></div></div>
  <div class="thumb"><div class="img" role="img" aria-label="Speckled light black and brown granite" style="background:linear-gradient(135deg,#c08a5c,#7a5a44,#d09a6c)"></div></div>
  <div class="thumb"><div class="img" role="img" aria-label="Light white and brown granite" style="background:linear-gradient(135deg,#a89372,#d3b98a,#a38c6a)"></div></div>
  <div class="thumb"><div class="img" role="img" aria-label="Off white and brown veined granite" style="background:linear-gradient(135deg,#9a8272,#b7a18f,#8e7565)"></div></div>
</div>
<div class="abs thumb-caption active" style="left:134px">Forest Shower - Brwon Color</div>
<div class="abs thumb-caption" style="left:370px">Light Black - Brwon Color</div>
<div class="abs thumb-caption" style="left:604px">Light White - Brwon Color</div>
<div class="abs thumb-caption" style="left:834px">Off White - Brwon Color</div>

<section class="abs content"></section>
<h2 class="abs intro-title" style="font-weight:400">Welcome to Stonecrest Granite ipsum dolor sit amet, consec adipiscing elit. Nulla auctor tincidunt.</h2>
<p class="abs intro-text">Proin dictum accumsan condimentum. In nec metus odio. Aliquam rutrum diam quis odio adipiscing facilisis. Sed porttitor condimentum interdum. In vehicula porta tortor, at faucibus nunc pulvinar consectetur. Nam dignissim, lectus vitae bibendum tempus, arcu nunc auctor neque, eu fringilla nisl nulla vel eros.</p>
<h3 class="abs showcase-title" style="font-weight:400">Our Product Showcase</h3>

<div class="abs tile" style="left:160px" role="img" aria-label="Golden speckled granite sample"><div style="width:100%;height:100%;background:linear-gradient(135deg,#c9a46a,#8f7044,#d6b27a)"></div><div class="arrow"><svg width="8" height="13"><path d="M1 1l6 5.5L1 12" fill="none" stroke="#333" stroke-width="1.3"/></svg></div></div>
<div class="abs tile" style="left:302.5px" role="img" aria-label="Cracked sandstone sample"><div style="width:100%;height:100%;background:linear-gradient(135deg,#c9a277,#b48c62,#d2ac80)"></div><div class="arrow"><svg width="8" height="13"><path d="M1 1l6 5.5L1 12" fill="none" stroke="#333" stroke-width="1.3"/></svg></div></div>
<div class="abs tile" style="left:445px" role="img" aria-label="Pink speckled granite sample"><div style="width:100%;height:100%;background:linear-gradient(135deg,#c9937c,#b3806c,#d0a08a)"></div><div class="arrow"><svg width="8" height="13"><path d="M1 1l6 5.5L1 12" fill="none" stroke="#333" stroke-width="1.3"/></svg></div></div>
<div class="abs tile" style="left:587.5px" role="img" aria-label="Dark brown and amber granite sample"><div style="width:100%;height:100%;background:linear-gradient(135deg,#5a3f30,#b27a4c,#4b3428)"></div><div class="arrow"><svg width="8" height="13"><path d="M1 1l6 5.5L1 12" fill="none" stroke="#333" stroke-width="1.3"/></svg></div></div>

<div class="abs sale" role="img" aria-label="Bedroom interior promotion banner">
  <div class="l1">SALE UNTIL DEC 2011</div>
  <div class="l2">UPTO 60% OFF</div>
</div>
<div class="abs cta cta-blue">Have Any Questions <svg width="9" height="13"><path d="M1.5 1.5l5 5-5 5" fill="none" stroke="#fff" stroke-width="2"/></svg></div>
<div class="abs cta cta-grey1">Get a Quick Quote <svg width="9" height="13"><path d="M1.5 1.5l5 5-5 5" fill="none" stroke="#fff" stroke-width="2"/></svg></div>
<div class="abs cta cta-grey2">Select Colors <svg width="9" height="13"><path d="M1.5 1.5l5 5-5 5" fill="none" stroke="#fff" stroke-width="2"/></svg></div>
<div class="abs side-tab">GET A QUICK QUOTE</div>

<footer class="abs footer"></footer>
<div class="abs foot-bar foot-bar-1"><span>Home</span><span>About Us</span><span>Gallery</span><span>Questions</span><span>Order</span><span>Shoping Cart</span></div>
<div class="abs foot-bar foot-bar-2"><span>Return Policy</span><span>Shipping Policy</span><span>Privacy</span><span>Terms of Use</span><span>Customer Service</span></div>
<div class="abs copyright">All Rights Reserved © Copyright with Stonecrest Granite - 2011 <span>Powered by : Pixelcraft Studio</span></div>
<div class="abs social" style="top:1070px">Share with us Facenote <span class="dot"></span></div>
<div class="abs social" style="top:1098px">Follow us on Chirper <span class="dot"></span></div>
<div class="abs social" style="top:1126px">Join us on Linkwork <span class="dot"></span></div>
</body>
</html>
```